" Já possuo três empresas: vartelo.com.br, lumarqa.com.br/site e tavorisena.com.br. O objetivo desta nova empresa é oferecer cursos via plataforma Prumvix. Diversos professores e profissionais irão gravar vídeo-aulas em diversos temas da Psicologia e disponibilizar na plataforma. O cliente poderá comprar cursos separados ou uma sequencia de cursos (pacotes). "

```html
<!DOCTYPE html>
<html lang="pt-BR">
<head>
<meta charset="utf-8">
<title>Mentara EaD – Assinatura de e-mail</title>
<link href="https://fonts.googleapis.com/css2?family=Montserrat:wght@500;600;700&family=Arimo:wght@400;700&display=swap" rel="stylesheet">
<style>
  :root{
    --navy:#3b5280;
    --ink:#3a3a3a;
    --muted:#555b66;
    --paper:#ffffff;
    --backdrop:#e6e6e6;
    --band:#d9dbe0;
    --mark:#b9bcc3;
  }
  *{margin:0;padding:0;box-sizing:border-box}
  html,body{width:1200px;height:1200px;overflow:hidden}
  body{background:var(--backdrop);position:relative;font-family:"Arimo",Arial,sans-serif}

  .signature{position:absolute;left:108px;width:984px;height:312px;background:var(--paper);
    border-radius:24px;overflow:hidden;box-shadow:0 8px 24px rgba(0,0,0,.12)}
  .signature--light{top:204px}
  .signature--dark{top:592px}
  .signature__panel{position:absolute;inset:0;width:100%;height:100%}

  .brand{position:absolute;left:72px;top:118px}
  .brand__row{display:flex;align-items:center;gap:10px}
  .brand__dot{width:26px;height:26px;border-radius:50%;background:var(--mark)}
  .brand__name{font-family:"Montserrat",Arial,sans-serif;font-weight:700;font-size:38px;
    color:var(--navy);letter-spacing:-.5px;line-height:1}
  .brand__tagline{font-family:"Montserrat",Arial,sans-serif;font-weight:700;font-size:10px;
    color:var(--ink);margin-top:12px;letter-spacing:.2px}
  .social{display:flex;gap:12px;margin-top:16px}
  .social__dot{width:24px;height:24px;border-radius:50%;background:var(--navy)}

  .contact{position:absolute;right:134px;top:0;bottom:0;width:340px;text-align:right;color:var(--ink)}
  .contact > *{position:absolute;right:0;white-space:nowrap}
  .contact__name{top:28px;font-family:"Montserrat",Arial,sans-serif;font-weight:600;font-size:24px;color:var(--navy);line-height:1.1}
  .contact__role{top:58px;font-family:"Montserrat",Arial,sans-serif;font-weight:700;font-size:13px;color:var(--muted)}
  .contact__block{font-size:14px;line-height:17px}
  .contact__block--phone{top:100px}
  .contact__block--web{top:166px}
  .contact__block--address{top:212px}

  .icon{position:absolute;left:874px;width:28px;height:28px;border-radius:6px;background:var(--navy);
    display:flex;align-items:center;justify-content:center}
  .icon svg{width:18px;height:18px}
  .icon--phone{top:114px}
  .icon--web{top:180px}
  .icon--pin{top:244px}

  .signature--dark .contact,.signature--dark .contact__name,.signature--dark .contact__role{color:#fff}
  .signature--dark .icon{background:#fff}
</style>
</head>
<body>

<section class="signature signature--light">
  <div class="brand">
    <div class="brand__row"><span class="brand__dot"></span><span class="brand__name">Mentara EaD</span></div>
    <p class="brand__tagline">CURSOS ONLINE DE PSICOLOGIA</p>
    <div class="social"><span class="social__dot"></span><span class="social__dot"></span><span class="social__dot"></span></div>
  </div>
  <div class="contact">
    <p class="contact__name">NOME SOBRENOME</p>
    <p class="contact__role">CARGO - FUNÇÃO</p>
    <p class="contact__block contact__block--phone">+55 (11) 99999-9999<br>+55 (11) 9999-9999</p>
    <p class="contact__block contact__block--web">email@seuemail.com.br<br>www.site.com.br</p>
    <p class="contact__block contact__block--address">Mentara EaD<br>End: SHCS CR Qd 702,<br>Bloco F, Entr 12 (pela W3 Sul)<br>Asa Sul, Brasília-DF</p>
  </div>
  <div class="icon icon--phone"><svg viewBox="0 0 24 24"><path fill="#fff" d="M6.6 10.8a15 15 0 0 0 6.6 6.6l2.2-2.2c.3-.3.7-.4 1-.2 1.1.4 2.3.6 3.6.6.6 0 1 .4 1 1V20c0 .6-.4 1-1 1A17 17 0 0 1 3 4c0-.6.4-1 1-1h3.5c.6 0 1 .4 1 1 0 1.3.2 2.5.6 3.6.1.3 0 .7-.2 1z"/></svg></div>
  <div class="icon icon--web"><svg viewBox="0 0 24 24" fill="none" stroke="#fff" stroke-width="1.8"><circle cx="12" cy="12" r="9"/><path d="M3 12h18M12 3c3 3 3 15 0 18M12 3c-3 3-3 15 0 18"/></svg></div>
  <div class="icon icon--pin"><svg viewBox="0 0 24 24"><path fill="#fff" d="M12 2a7 7 0 0 0-7 7c0 5 7 13 7 13s7-8 7-13a7 7 0 0 0-7-7zm0 9.5A2.5 2.5 0 1 1 12 6.5a2.5 2.5 0 0 1 0 5z"/></svg></div>
</section>

<section class="signature signature--dark">
  <svg class="signature__panel" viewBox="0 0 984 312" preserveAspectRatio="none" aria-hidden="true">
    <path d="M350 0 H984 V312 H560 C490 250 390 115 350 0Z" fill="var(--band)"/>
    <path d="M380 0 H984 V312 H590 C520 250 420 115 380 0Z" fill="var(--navy)"/>
  </svg>
  <div class="brand">
    <div class="brand__row"><span class="brand__dot"></span><span class="brand__name">Mentara EaD</span></div>
    <p class="brand__tagline">CURSOS ONLINE DE PSICOLOGIA</p>
    <div class="social"><span class="social__dot"></span><span class="social__dot"></span><span class="social__dot"></span></div>
  </div>
  <div class="contact">
    <p class="contact__name">NOME SOBRENOME</p>
    <p class="contact__role">CARGO - FUNÇÃO</p>
    <p class="contact__block contact__block--phone">+55 (11) 99999-9999<br>+55 (11) 9999-9999</p>
    <p class="contact__block contact__block--web">email@seuemail.com.br<br>www.site.com.br</p>
    <p class="contact__block contact__block--address">Mentara EaD<br>End: SHCS CR Qd 702,<br>Bloco F, Entr 12 (pela W3 Sul)<br>Asa Sul, Brasília-DF</p>
  </div>
  <div class="icon icon--phone"><svg viewBox="0 0 24 24"><path fill="#3b5280" d="M6.6 10.8a15 15 0 0 0 6.6 6.6l2.2-2.2c.3-.3.7-.4 1-.2 1.1.4 2.3.6 3.6.6.6 0 1 .4 1 1V20c0 .6-.4 1-1 1A17 17 0 0 1 3 4c0-.6.4-1 1-1h3.5c.6 0 1 .4 1 1 0 1.3.2 2.5.6 3.6.1.3 0 .7-.2 1z"/></svg></div>
  <div class="icon icon--web"><svg viewBox="0 0 24 24" fill="none" stroke="#3b5280" stroke-width="1.8"><circle cx="12" cy="12" r="9"/><path d="M3 12h18M12 3c3 3 3 15 0 18M12 3c-3 3-3 15 0 18"/></svg></div>
  <div class="icon icon--pin"><svg viewBox="0 0 24 24"><path fill="#3b5280" d="M12 2a7 7 0 0 0-7 7c0 5 7 13 7 13s7-8 7-13a7 7 0 0 0-7-7zm0 9.5A2.5 2.5 0 1 1 12 6.5a2.5 2.5 0 0 1 0 5z"/></svg></div>
</section>

</body>
</html>
```